Business Card Design

Attached is the logo of the store.

Information needed on the business card:

www.brookvale17vino.com
info@brookvale17vino.com
412 Harlow St NY, NY 10027
Tel:(646) 472-3958

Store Hours
Mon-Sat Noon-10pm
Sun Noon-8pm

Free Deliveries

Industry/Entity Type

Business

Contact Information for Business Card

Brookvale 17 Wine & Spirits

```html
<!DOCTYPE html>
<html lang="en">
<head>
<meta charset="utf-8">
<title>Brookvale 17 Wine &amp; Spirits – Business Card</title>
<link rel="stylesheet" href="https://fonts.googleapis.com/css2?family=Questrial&display=swap">
<style>
  :root {
    --canvas: #e9e6e2;
    --card-white: #ffffff;
    --card-black: #231f20;
    --ink-light: #ffffff;
    --ink-dark: #231f20;
    --accent-red: #e31b3b;
    --shadow: rgba(0, 0, 0, 0.28);
  }
  * { box-sizing: border-box; margin: 0; padding: 0; }
  html, body {
    width: 1200px;
    height: 1000px;
    overflow: hidden;
    background: var(--canvas);
    font-family: "Questrial", "Century Gothic", sans-serif;
  }
  .canvas {
    position: relative;
    width: 1200px;
    height: 1000px;
  }
  .card {
    position: absolute;
    width: 580px;
    height: 332px;
    box-shadow: 0 10px 26px var(--shadow);
    overflow: hidden;
  }

  /* Front side: white card with black band */
  .card-front {
    left: 70px;
    top: 90px;
    background: var(--card-white);
  }
  .card-front .band {
    position: absolute;
    left: 0;
    top: 62px;
    width: 100%;
    height: 150px;
    background: var(--card-black);
  }
  .card-front .brand {
    position: absolute;
    left: 34px;
    top: 110px;
    color: var(--ink-light);
    line-height: 1.1;
  }
  .card-front .brand-name { font-size: 34px; display: block; }
  .card-front .brand-tag { font-size: 17px; display: block; }
  .contact {
    position: absolute;
    left: 300px;
    top: 82px;
    color: var(--ink-light);
    font-size: 16.5px;
    line-height: 1.45;
    list-style: none;
  }
  .contact .web {
    color: var(--accent-red);
    font-weight: 700;
    font-size: 18px;
    letter-spacing: 0.2px;
  }
  .hours {
    position: absolute;
    left: 300px;
    top: 226px;
    color: var(--ink-dark);
    font-size: 17px;
    line-height: 1.35;
  }
  .hours .delivery {
    margin-top: 10px;
    color: var(--accent-red);
    font-weight: 700;
    font-size: 19px;
  }

  /* Back side: black card with centered name */
  .card-back {
    left: 560px;
    top: 560px;
    background: var(--card-black);
  }
  .card-back .brand {
    position: absolute;
    left: 0;
    right: 0;
    top: 110px;
    text-align: center;
    color: var(--ink-light);
    line-height: 1.15;
  }
  .card-back .brand-name { font-size: 58px; display: block; }
  .card-back .brand-tag { font-size: 26px; display: block; }
</style>
</head>
<body>
<main class="canvas">

  <section class="card card-front" aria-label="Business card front">
    <div class="band"></div>
    <div class="brand">
      <span class="brand-name">Brookvale 17</span>
      <span class="brand-tag">wine &amp; spirits</span>
    </div>
    <ul class="contact">
      <li class="web">www.brookvale17vino.com</li>
      <li>info@brookvale17vino.com</li>
      <li>412 Harlow St NY, NY 10027</li>
      <li>Tel:(646) 472-3958</li>
    </ul>
    <div class="hours">
      <p>Store Hours</p>
      <p>Mon-Sat Noon-10pm</p>
      <p>Sun Noon-8pm</p>
      <p class="delivery">Free Deliveries!</p>
    </div>
  </section>

  <section class="card card-back" aria-label="Business card back">
    <div class="brand">
      <span class="brand-name">Brookvale 17</span>
      <span class="brand-tag">wine &amp; spirits</span>
    </div>
  </section>

</main>
</body>
</html>
```